Maple Ridge business card design

Card needs to include the following text/items:
Company Logo
Tobin Marsh
Phone # - 555-318-7642
service@mapleridgelandscaping.example
Lawn & landscape maintenance services

```html
<!DOCTYPE html>
<html lang="en">
<head>
<meta charset="utf-8">
<title>Maple Ridge business card</title>
<link rel="stylesheet" href="https://fonts.googleapis.com/css2?family=Roboto+Condensed:wght@400;700&display=swap">
<style>
  :root {
    --backdrop: #e4e5e7;
    --card: #ffffff;
    --ink-green: #0f4d26;
    --band-dark: #1a6b37;
    --band-light: #5b9140;
    --ring: #7f9f3c;
  }
  * { margin: 0; padding: 0; box-sizing: border-box; }
  html, body {
    width: 969px;
    height: 1200px;
    overflow: hidden;
    background: var(--backdrop);
    font-family: "Roboto Condensed", sans-serif;
  }
  .canvas { position: relative; width: 969px; height: 1200px; }
  .card {
    position: absolute;
    left: 79px;
    width: 811px;
    height: 463px;
    background: var(--card);
    overflow: hidden;
  }
  .card--front { top: 79px; }
  .card--back { top: 635px; }
  .card__bands { position: absolute; inset: 0; width: 100%; height: 100%; }

  .brand { position: absolute; text-align: center; color: var(--ink-green); }
  .brand__mark { display: block; margin: 0 auto; }
  .brand__name { display: block; font-weight: 700; white-space: nowrap; line-height: 1; }

  .card--front .brand { left: 88px; top: 113px; width: 240px; }
  .card--front .brand__name { font-size: 42px; margin-top: 14px; }
  .card--back .brand { left: 205px; top: 52px; width: 400px; }
  .card--back .brand__name { font-size: 68px; margin-top: 34px; }

  .details { position: absolute; left: 411px; top: 118px; color: var(--ink-green); }
  .details__name { font-size: 51px; font-weight: 700; line-height: 1; letter-spacing: -0.3px; }
  .details__service { font-size: 28px; font-weight: 400; line-height: 29px; margin-top: 20px; }
  .details__contact { list-style: none; margin-top: 24px; }
  .details__contact li { display: flex; align-items: center; gap: 11px; font-size: 20px; line-height: 1; height: 30px; }
  .details__contact svg { flex: none; width: 22px; height: 22px; }
</style>
</head>
<body>
<div class="canvas">

  <section class="card card--front">
    <svg class="card__bands" viewBox="0 0 811 463" preserveAspectRatio="none" aria-hidden="true">
      <defs>
        <linearGradient id="band-top" x1="0" x2="1" y1="0" y2="0">
          <stop offset="0" stop-color="var(--band-dark)"/>
          <stop offset="1" stop-color="var(--band-light)"/>
        </linearGradient>
        <linearGradient id="band-bottom" x1="0" x2="1" y1="0" y2="0">
          <stop offset="0" stop-color="var(--band-light)"/>
          <stop offset="1" stop-color="var(--band-dark)"/>
        </linearGradient>
      </defs>
      <path d="M0 0 H811 V23 C560 16 250 20 0 89 Z" fill="url(#band-top)"/>
      <path d="M0 463 H811 V374 C640 430 360 444 0 441 Z" fill="url(#band-bottom)"/>
    </svg>

    <div class="brand">
      <svg class="brand__mark" width="176" height="150" viewBox="0 0 176 150" aria-hidden="true">
        <circle cx="88" cy="88" r="85" fill="none" stroke="var(--ring)" stroke-width="3"/>
      </svg>
      <span class="brand__name">Maple Ridge</span>
    </div>

    <div class="details">
      <h1 class="details__name">Tobin Marsh</h1>
      <p class="details__service">Lawn &amp; landscape<br>maintenance services</p>
      <ul class="details__contact">
        <li>
          <svg viewBox="0 0 24 24" aria-hidden="true"><path fill="var(--ink-green)" d="M6.6 2.5c.6-.4 1.4-.3 1.8.3l2.4 3.6c.4.6.3 1.4-.2 1.9l-1.7 1.5c1 2.2 2.9 4.2 5.2 5.3l1.5-1.7c.5-.5 1.3-.6 1.9-.2l3.6 2.4c.6.4.8 1.2.4 1.8l-1.3 2.2c-.6 1-1.8 1.5-3 1.2C10.6 19.3 4.7 13.4 3.2 6.8c-.3-1.2.2-2.4 1.2-3z"/></svg>
          555-318-7642
        </li>
        <li>
          <svg viewBox="0 0 24 24" aria-hidden="true"><rect x="2" y="5" width="20" height="14" fill="none" stroke="var(--ink-green)" stroke-width="2"/><path d="M2 5l10 8 10-8M2 19l7.5-7M22 19l-7.5-7" fill="none" stroke="var(--ink-green)" stroke-width="2"/></svg>
          service@mapleridgelandscaping.example
        </li>
      </ul>
    </div>
  </section>

  <section class="card card--back">
    <div class="brand">
      <svg class="brand__mark" width="276" height="240" viewBox="0 0 276 240" aria-hidden="true">
        <circle cx="138" cy="138" r="135" fill="none" stroke="var(--ring)" stroke-width="4"/>
      </svg>
      <span class="brand__name">Maple Ridge</span>
    </div>
  </section>

</div>
</body>
</html>
```